Rack card 4"x9" for a construction company

We need to have a design for:
- the holder of rack cards. Letter size
- and the rack cards. Size 4"x9"

I attached a picture of the sample holder for example.

I am putting some of the brochures and pics we have in:

https://files.vendoshare.net/folders/7QpT3wXz9KmB2rLvN8cYd4HsJ6fGaE5uVo?usp=sharing

The Bodoni font is on the drive.
The rack card should call to action - to learn about our projects and that we are offering fixed price packages.

One of the sides of the rack card has to show our houses like we show on the website birchwell-builders.ca
Images with short info like on the website http://www.birchwell-builders.ca/our-projects/
Maybe have something like: Learn more about our recent projects at www...

You can use our logo from th pdf files. In the brochure on the cover page we show all the associations we are member of - this is a must to be shown.

Mentioning the website and the phone number is a must.

Bring your ideas.
Don't hesitate to ask questions.

Thanks
Dorian

```html
<!DOCTYPE html>
<html lang="en">
<head>
<meta charset="utf-8">
<title>Birchwell Builders – Rack Card Holder</title>
<link rel="stylesheet" href="https://fonts.googleapis.com/css2?family=Libre+Bodoni:wght@700&family=Roboto:wght@300;400&display=swap">
<style>
:root{
  --navy:#0d1b3e;
  --green:#6aaa5f;
  --icon-green:#8dc87c;
  --tan:#b6a98b;
  --khaki:#a9a68a;
  --sky:#7d9bd6;
  --panel:#e7e7e7;
  --border:#d3d3d3;
  --text:#2b2b2b;
  --white:#ffffff;
}
*{margin:0;padding:0;box-sizing:border-box}
html,body{width:936px;height:1200px;overflow:hidden;background:var(--white)}
.card{position:relative;width:936px;height:1200px;background:var(--white);font-family:"Roboto",Arial,sans-serif;color:var(--text)}
.serif{font-family:"Libre Bodoni","Bodoni Moda",Georgia,serif;font-weight:700}

.header{position:absolute;left:0;top:0;width:936px;height:165px;background:var(--navy)}
.brand{position:absolute;left:0;top:0;width:220px;height:165px;background:var(--panel);display:flex;align-items:center;justify-content:center;text-align:center}
.brand-name{font-family:"Libre Bodoni",Georgia,serif;font-weight:700;color:var(--navy);font-size:27px;line-height:1.15;letter-spacing:1px}
.headline{position:absolute;left:220px;top:0;width:716px;height:165px;display:flex;align-items:center;justify-content:center;text-align:center;color:var(--white);font-size:40px;line-height:46px;letter-spacing:1.5px}

.intro{position:absolute;left:37px;top:203px;width:400px}
.intro h2{font-size:31px;line-height:36px;color:var(--navy);letter-spacing:.8px}
.intro h2 .accent{color:var(--green)}
.intro .rule{width:108px;height:2px;background:var(--navy);margin:12px 0 30px}
.intro p{font-weight:300;font-size:17.5px;line-height:22px;color:#333}

.photo{position:absolute}
.hero{left:467px;top:181px;width:469px;height:257px;background:
  radial-gradient(ellipse 45% 60% at 45% 55%,rgba(235,232,226,.95) 0%,rgba(200,200,205,.6) 55%,rgba(200,200,205,0) 100%),
  linear-gradient(180deg,#1f3f92 0%,#3d5fae 40%,#6f7d8c 70%,#55763f 100%)}
.p1{background:
  radial-gradient(ellipse 40% 55% at 52% 50%,rgba(232,230,224,.95) 0%,rgba(232,230,224,0) 100%),
  linear-gradient(180deg,#22419a 0%,#4a68b0 45%,#7a7f84 75%,#4f7a3c 100%)}
.p2{background:
  radial-gradient(ellipse 50% 45% at 50% 45%,rgba(70,72,78,.9) 0%,rgba(70,72,78,0) 100%),
  linear-gradient(180deg,#c7d8ea 0%,#8c949c 40%,#5b5e63 65%,#7f9670 100%)}
.p3{background:
  radial-gradient(ellipse 42% 55% at 48% 55%,rgba(150,156,168,.9) 0%,rgba(150,156,168,0) 100%),
  linear-gradient(180deg,#17307a 0%,#2f4b96 45%,#5a606b 80%,#3e4048 100%)}
.p4{background:
  radial-gradient(ellipse 40% 55% at 45% 50%,rgba(62,66,74,.95) 0%,rgba(62,66,74,0) 100%),
  linear-gradient(180deg,#e2ebf3 0%,#a9b2bb 40%,#6a6e75 70%,#5f8249 100%)}

.project{position:absolute;border:2px solid var(--border);background:var(--white);padding:11px 10px 0 12px}
.project h3{font-size:17.5px;line-height:22px;color:var(--navy);letter-spacing:-.2px;white-space:nowrap}
.project .tick{width:30px;height:2px;background:var(--tan);margin:6px 0 8px}
.project .notick{height:16px}
.specs{display:flex;justify-content:space-between;padding-right:2px}
.spec{display:flex;flex-direction:column;align-items:center;width:56px}
.spec svg{width:30px;height:20px}
.spec .val{font-size:18px;color:#333;margin-top:10px;white-space:nowrap}
.spec .val small{font-size:11px}

.members{position:absolute;left:339px;top:792px;width:257px;height:30px;border-radius:15px;background:var(--panel);display:flex;align-items:center;justify-content:center;color:var(--navy);font-size:16px;letter-spacing:.5px}
.badge{position:absolute}
.b1{left:36px;top:860px;width:120px;height:72px;border-radius:50%;background:#2f5fa8}
.b2{left:224px;top:856px;width:114px;height:80px;border-radius:6px;background:#c9282f}
.b3{left:404px;top:850px;width:96px;height:96px;border-radius:4px;background:#1e8a3c}
.b4{left:560px;top:852px;width:110px;height:92px;border-radius:4px;background:#1c2e6b}
.b5{left:748px;top:870px;width:142px;height:50px;border-radius:6px;background:#1e5aa0}

.footer{position:absolute;left:0;top:986px;width:936px;height:214px;background:var(--navy);color:var(--white);text-align:center}
.bump{position:absolute;left:421px;top:940px;width:94px;height:94px;border-radius:50%;background:var(--navy)}
.learn{position:absolute;top:24px;width:100%;font-size:21px}
.learn .soft{color:var(--khaki)}
.touch{position:absolute;top:56px;width:100%;display:flex;align-items:center;justify-content:center;gap:18px;font-size:30px}
.touch .line{width:48px;height:2px;background:var(--white)}
.touch .hi{color:var(--sky)}
.contact{position:absolute;width:100%;display:flex;justify-content:center;align-items:center;gap:10px;font-size:20px}
.contact svg{width:22px;height:22px}
.c1{top:98px}.c2{top:130px}.c3{top:162px}
.contact .gap{width:14px}
</style>
</head>
<body>
<div class="card">
  <header class="header">
    <div class="brand"><div class="brand-name">BIRCHWELL<br>BUILDERS</div></div>
    <h1 class="headline serif">BUILD THE HOME OF YOUR<br>DREAMS IN VANCOUVER</h1>
  </header>

  <section class="intro">
    <h2 class="serif">MAKING YOUR DREAM<br><span class="accent">HOME A REALITY.</span></h2>
    <div class="rule"></div>
    <p>If you want the home of your dreams to move seamlessly from vision to reality, it’s vital that you partner with a builder with the ability – and the capacity – to guide you through each step of the building process.</p>
  </section>

  <div class="photo hero" role="img" aria-label="Photo of a white modern luxury home lit at dusk"></div>

  <div class="photo p1" role="img" aria-label="Photo of the Kerrisdale modern home at dusk" style="left:28px;top:456px;width:213px;height:153px"></div>
  <article class="project" style="left:246px;top:456px;width:217px;height:153px">
    <h3 class="serif">Kerrisdale<br>Modern Opulence</h3>
    <div class="notick"></div>
    <div class="specs">
      <div class="spec"><svg viewBox="0 0 32 22"><rect x="2" y="4" width="3" height="16" fill="#b6a98b"/><rect x="5" y="12" width="25" height="4" fill="#b6a98b"/><rect x="27" y="12" width="3" height="8" fill="#b6a98b"/><rect x="6" y="8" width="7" height="4" fill="#b6a98b"/></svg><span class="val">4</span></div>
      <div class="spec"><svg viewBox="0 0 32 22"><rect x="4" y="9" width="24" height="4" fill="#b6a98b"/><path d="M6 13h20l-2 5H8z" fill="#b6a98b"/><rect x="6" y="2" width="2" height="7" fill="#b6a98b"/><rect x="8" y="2" width="4" height="2" fill="#b6a98b"/></svg><span class="val">6</span></div>
      <div class="spec"><svg viewBox="0 0 32 22"><path d="M6 20L26 2v18z" fill="none" stroke="#b6a98b" stroke-width="2.5"/><path d="M16 20l5-5v5z" fill="#b6a98b"/></svg><span class="val">3,242<small> sqft</small></span></div>
    </div>
  </article>

  <div class="photo p2" role="img" aria-label="Photo of the Burnaby craftsman home with stone facade" style="left:469px;top:456px;width:213px;height:153px"></div>
  <article class="project" style="left:687px;top:456px;width:214px;height:153px">
    <h3 class="serif">Burnaby<br>Modern Craftsman</h3>
    <div class="tick"></div>
    <div class="specs">
      <div class="spec"><svg viewBox="0 0 32 22"><rect x="2" y="4" width="3" height="16" fill="#b6a98b"/><rect x="5" y="12" width="25" height="4" fill="#b6a98b"/><rect x="27" y="12" width="3" height="8" fill="#b6a98b"/><rect x="6" y="8" width="7" height="4" fill="#b6a98b"/></svg><span class="val">8</span></div>
      <div class="spec"><svg viewBox="0 0 32 22"><rect x="4" y="9" width="24" height="4" fill="#b6a98b"/><path d="M6 13h20l-2 5H8z" fill="#b6a98b"/><rect x="6" y="2" width="2" height="7" fill="#b6a98b"/><rect x="8" y="2" width="4" height="2" fill="#b6a98b"/></svg><span class="val">8</span></div>
      <div class="spec"><svg viewBox="0 0 32 22"><path d="M6 20L26 2v18z" fill="none" stroke="#b6a98b" stroke-width="2.5"/><path d="M16 20l5-5v5z" fill="#b6a98b"/></svg><span class="val">4,740<small> sqft</small></span></div>
    </div>
  </article>

  <div class="photo p3" role="img" aria-label="Photo of the Renfrew modern craftsman home at night" style="left:28px;top:613px;width:213px;height:158px"></div>
  <article class="project" style="left:246px;top:613px;width:217px;height:158px">
    <h3 class="serif">Renfrew<br>Modern Craftsman</h3>
    <div class="notick" style="height:19px"></div>
    <div class="specs">
      <div class="spec"><svg viewBox="0 0 32 22"><rect x="2" y="4" width="3" height="16" fill="#b6a98b"/><rect x="5" y="12" width="25" height="4" fill="#b6a98b"/><rect x="27" y="12" width="3" height="8" fill="#b6a98b"/><rect x="6" y="8" width="7" height="4" fill="#b6a98b"/></svg><span class="val">9</span></div>
      <div class="spec"><svg viewBox="0 0 32 22"><rect x="4" y="9" width="24" height="4" fill="#b6a98b"/><path d="M6 13h20l-2 5H8z" fill="#b6a98b"/><rect x="6" y="2" width="2" height="7" fill="#b6a98b"/><rect x="8" y="2" width="4" height="2" fill="#b6a98b"/></svg><span class="val">7</span></div>
      <div class="spec"><svg viewBox="0 0 32 22"><path d="M6 20L26 2v18z" fill="none" stroke="#b6a98b" stroke-width="2.5"/><path d="M16 20l5-5v5z" fill="#b6a98b"/></svg><span class="val">3,637<small> sqft</small></span></div>
    </div>
  </article>

  <div class="photo p4" role="img" aria-label="Rendering of the Renfrew traditional craftsman home" style="left:469px;top:613px;width:213px;height:158px"></div>
  <article class="project" style="left:687px;top:613px;width:214px;height:158px">
    <h3 class="serif">Renfrew<br>Traditional Craftsman</h3>
    <div class="tick" style="margin-bottom:11px"></div>
    <div class="specs">
      <div class="spec"><svg viewBox="0 0 32 22"><rect x="2" y="4" width="3" height="16" fill="#b6a98b"/><rect x="5" y="12" width="25" height="4" fill="#b6a98b"/><rect x="27" y="12" width="3" height="8" fill="#b6a98b"/><rect x="6" y="8" width="7" height="4" fill="#b6a98b"/></svg><span class="val">7</span></div>
      <div class="spec"><svg viewBox="0 0 32 22"><rect x="4" y="9" width="24" height="4" fill="#b6a98b"/><path d="M6 13h20l-2 5H8z" fill="#b6a98b"/><rect x="6" y="2" width="2" height="7" fill="#b6a98b"/><rect x="8" y="2" width="4" height="2" fill="#b6a98b"/></svg><span class="val">5</span></div>
      <div class="spec"><svg viewBox="0 0 32 22"><path d="M6 20L26 2v18z" fill="none" stroke="#b6a98b" stroke-width="2.5"/><path d="M16 20l5-5v5z" fill="#b6a98b"/></svg><span class="val">2,679<small> sqft</small></span></div>
    </div>
  </article>

  <div class="members serif">PROUD MEMBERS OF</div>
  <div class="badge b1" role="img" aria-label="Home builders association membership badge"></div>
  <div class="badge b2" role="img" aria-label="Home warranty provider badge"></div>
  <div class="badge b3" role="img" aria-label="National home builders association member badge"></div>
  <div class="badge b4" role="img" aria-label="2-5-10 year warranty badge"></div>
  <div class="badge b5" role="img" aria-label="Accredited business badge"></div>

  <div class="bump"></div>
  <footer class="footer">
    <div class="learn serif">Learn more about <span class="soft">our recent projects</span></div>
    <div class="touch serif"><span class="line"></span><span><span class="hi">Get In Touch</span> With Us</span><span class="line"></span></div>
    <div class="contact c1">
      <svg viewBox="0 0 22 22"><circle cx="11" cy="11" r="10" fill="none" stroke="#8dc87c" stroke-width="1.5"/><path d="M11 17s-4-4.5-4-7.5a4 4 0 0 1 8 0c0 3-4 7.5-4 7.5z" fill="#8dc87c"/><circle cx="11" cy="9.5" r="1.4" fill="#0d1b3e"/></svg>
      <span>#310-4820 Harbour Avenue, Vancouver, BC V6N 2K4</span>
    </div>
    <div class="contact c2">
      <svg viewBox="0 0 22 22"><circle cx="11" cy="11" r="10" fill="none" stroke="#8dc87c" stroke-width="1.5"/><path d="M8 6c-1 1-1 3 0 5s3 4 5 5c1 .5 2 0 2.5-.8l-2-1.5-1 .8c-1-.5-2.5-2-3-3l.8-1-1.5-2z" fill="#8dc87c"/></svg>
      <span>604.555.0187</span><span class="gap"></span>
      <svg viewBox="0 0 22 22"><circle cx="11" cy="11" r="10" fill="none" stroke="#8dc87c" stroke-width="1.5"/><rect x="6" y="7.5" width="10" height="7" fill="none" stroke="#8dc87c" stroke-width="1.3"/><path d="M6 7.5l5 4 5-4" fill="none" stroke="#8dc87c" stroke-width="1.3"/></svg>
      <span>contact@birchwell-builders.ca</span>
    </div>
    <div class="contact c3">
      <svg viewBox="0 0 22 22"><circle cx="11" cy="11" r="9.5" fill="none" stroke="#8dc87c" stroke-width="1.5"/><ellipse cx="11" cy="11" rx="4" ry="9.5" fill="none" stroke="#8dc87c" stroke-width="1.2"/><path d="M1.5 11h19M3 6.5h16M3 15.5h16" stroke="#8dc87c" stroke-width="1.2"/></svg>
      <span>www.birchwell-builders.ca</span>
    </div>
  </footer>
</div>
</body>
</html>
```